Etiketten-Design für Weißwein
Zielgruppe
Wir betreiben einen Weingroßhandel, beliefern die Gastronomie mit Wein und haben einen Onlineshop unter kerstel-wein.de
Zielgruppe für diesen Wein: Gastronomie und Privatkunden, Altersgruppe: 25-40, Charakteristiken: jung, aufgeschlossen und lebenslustig.
Aufgabenstellung
Zum Produkt: Flaschenform Bordeauxflasche, Inhalt Weißwein feinherb und wertig von einem Top Weingut, als Sommerwein gedacht.
Das Etikett soll modern sein und auffallen. Unsere erste Idee war MIRAVELLO mit einem Spruch: Kein Ziel, kein Plan, aber fantastischen Wein. Wir freuen uns aber auch über neue Ideen.
u.U. könnten weitere Weine mit diesem Etikett mit leichten Anpassungen entstehen (z.B. ein Rotwein und ein Rose)

```html
<!DOCTYPE html>
<html lang="de">
<head>
<meta charset="utf-8">
<title>MIRAVELLO – Weißwein feinherb</title>
<link rel="stylesheet" href="https://fonts.googleapis.com/css2?family=Bebas+Neue&family=Oswald:wght@400&display=swap">
<style>
  :root {
    --label-white: #ffffff;
    --sage-green: #bddcbc;
    --ink-black: #1b1b1b;
  }
  html, body {
    margin: 0;
    padding: 0;
    width: 820px;
    height: 1200px;
    overflow: hidden;
    background: var(--label-white);
  }
  .wine-label {
    display: block;
    width: 820px;
    height: 1200px;
  }
  .sage-panel { fill: var(--sage-green); }
  .brand-name {
    font-family: "Bebas Neue", "Oswald", sans-serif;
    fill: var(--ink-black);
  }
  .tagline {
    font-family: "Bebas Neue", "Oswald", sans-serif;
    fill: var(--ink-black);
  }
  .wine-type {
    font-family: "Oswald", sans-serif;
    font-weight: 400;
    fill: var(--ink-black);
  }
</style>
</head>
<body>
<svg class="wine-label" viewBox="0 0 820 1200" xmlns="http://www.w3.org/2000/svg" role="img" aria-label="Weinetikett MIRAVELLO, Weißwein feinherb">
  <rect class="sage-panel" x="0" y="0" width="352" height="1200"/>

  <text class="brand-name" transform="translate(262 1120) rotate(-90)" x="0" y="0" font-size="240" textLength="1020" lengthAdjust="spacingAndGlyphs">MIRAVELLO</text>

  <g class="tagline-block">
    <text class="tagline" transform="translate(627 840) rotate(-90)" x="0" y="0" font-size="73" textLength="664" lengthAdjust="spacingAndGlyphs">OHNE EILE, OHNE ZWECK –</text>
    <text class="tagline" transform="translate(704 840) rotate(-90)" x="0" y="0" font-size="73" textLength="664" lengthAdjust="spacingAndGlyphs">DAFÜR HERRLICHER WEIN</text>
  </g>

  <g class="wine-type-block">
    <text class="wine-type" x="528" y="1006" font-size="46" textLength="189" lengthAdjust="spacingAndGlyphs">WEISSWEIN</text>
    <text class="wine-type" x="528" y="1085" font-size="46" textLength="166" lengthAdjust="spacingAndGlyphs">FEINHERB</text>
  </g>
</svg>
</body>
</html>
```